"Road work ahead" Paving Business card design

We own a paving business residential and commercial. We want to appeal to small homeowner and also to a larger professional company - driveway to home and parking lot. We also like dump trucks.The asphalt look is important that is what we mainly do.

Target Market(s)

Residential and Commercial

Industry/Entity Type

Business

Contact Information for Business Card

Company info. (address, email, phone number)

Font styles to use
Sans Serif
Decorative

Colors
ec1f27
fbee3f
1b1b1b
474747

Requirements
Must have
• Business Logo/Name
• address: 4187 North Calder Lane
• Frederick, MD 21704
• business phone: 240.555.0193
• office: 301.555.0147
• fax: 301.555.0162
• www.TQSurfacing.example
• Maryland's #1 Asphalt Specialist
• MHIC# 384072
• All Work Guaranteed
• Residential & Commercial
• Include: Roads-Driveways-Brick Pavers- Seal-Coating-Concrete-Asphalt Millings
• "Serving Central Maryland for over 15 years"
Nice to have
• Real life pictures that were included. The backround can be cut out if it doesn't look professional on the pictures they are not photo shopped. Would like to see the picture of all 3 trucks on the front of the card.

```html
<!DOCTYPE html>
<html lang="en">
<head>
<meta charset="utf-8">
<title>TQ Surfacing – Business Card</title>
<link rel="stylesheet" href="https://fonts.googleapis.com/css2?family=Fira+Sans:wght@400;600;800&display=swap">
<style>
  :root {
    --backdrop: #e6e6e6;
    --red-top: #e20404;
    --red-bottom: #6c0000;
    --brand-red: #ec1f27;
    --card-white: #f7f7f7;
    --card-grey: #ececec;
    --ink: #1b1b1b;
    --ink-soft: #474747;
    --white: #ffffff;
  }
  html, body {
    margin: 0;
    padding: 0;
    width: 1200px;
    height: 576px;
    overflow: hidden;
    background: var(--backdrop);
    font-family: "Fira Sans", sans-serif;
  }
  .canvas {
    position: relative;
    width: 1200px;
    height: 576px;
  }
  .card {
    position: absolute;
    top: 138px;
    width: 484px;
    height: 294px;
    border-radius: 14px;
    overflow: hidden;
  }
  .card-front {
    left: 82px;
    background: linear-gradient(180deg, var(--red-top) 0%, var(--red-bottom) 100%);
  }
  .card-back {
    left: 602px;
    width: 480px;
    background: linear-gradient(135deg, var(--card-white) 0%, var(--card-grey) 100%);
  }
  .brand {
    position: absolute;
    display: flex;
    align-items: center;
    gap: 10px;
    font-weight: 800;
    white-space: nowrap;
  }
  .card-front .brand {
    left: 50%;
    top: 146px;
    transform: translate(-50%, -50%);
    color: var(--white);
    font-size: 38px;
  }
  .card-front .brand-dot {
    width: 54px;
    height: 54px;
    border-radius: 50%;
    background: var(--white);
  }
  .front-tagline {
    position: absolute;
    left: 0;
    right: 0;
    top: 186px;
    margin: 0;
    text-align: center;
    color: var(--white);
    font-size: 14px;
    font-weight: 600;
    letter-spacing: 0.04em;
  }
  .front-footer {
    position: absolute;
    left: 0;
    right: 0;
    bottom: 18px;
    margin: 0;
    text-align: center;
    color: var(--white);
    font-size: 11px;
    letter-spacing: 0.06em;
    opacity: 0.9;
  }
  .card-back .brand {
    left: 22px;
    top: 122px;
    color: var(--brand-red);
    font-size: 28px;
  }
  .card-back .brand-dot {
    width: 40px;
    height: 40px;
    border-radius: 50%;
    background: var(--brand-red);
  }
  .contact {
    position: absolute;
    left: 289px;
    top: 64px;
    color: var(--ink);
  }
  .contact-name {
    margin: 0;
    font-size: 21px;
    font-weight: 600;
    line-height: 1.1;
  }
  .contact-title {
    margin: 2px 0 14px;
    font-size: 11px;
    color: var(--ink-soft);
  }
  .contact-list {
    list-style: none;
    margin: 0 0 10px;
    padding: 0;
  }
  .contact-list li {
    display: flex;
    align-items: center;
    gap: 12px;
    font-size: 12px;
    line-height: 16.5px;
  }
  .contact-list svg {
    width: 10px;
    height: 10px;
    fill: var(--brand-red);
  }
  .contact-address {
    margin: 0;
    font-size: 12px;
    line-height: 17px;
    font-style: normal;
  }
  .back-footer {
    position: absolute;
    left: 22px;
    right: 22px;
    bottom: 14px;
    padding-top: 7px;
    border-top: 1px solid #d6d6d6;
    color: var(--ink-soft);
    font-size: 9.5px;
    line-height: 14px;
    text-align: center;
  }
  .back-footer p { margin: 0; }
  .back-footer .credentials { color: var(--ink); font-weight: 600; }
</style>
</head>
<body>
<main class="canvas">
  <section class="card card-front" aria-label="Card front">
    <div class="brand">
      <span>TQ Surfacing</span>
      <span class="brand-dot"></span>
    </div>
    <p class="front-tagline">Maryland's #1 Asphalt Specialist</p>
    <p class="front-footer">Serving Central Maryland for over 15 years</p>
  </section>

  <section class="card card-back" aria-label="Card back">
    <div class="brand">
      <span>TQ Surfacing</span>
      <span class="brand-dot"></span>
    </div>

    <div class="contact">
      <h1 class="contact-name">Tom Quinlan</h1>
      <p class="contact-title">Managing Director</p>
      <ul class="contact-list">
        <li>
          <svg viewBox="0 0 10 10" aria-hidden="true"><rect x="2" y="0" width="6" height="10" rx="1"/><rect x="3" y="1.5" width="4" height="6" fill="#f7f7f7"/></svg>
          240.555.0193
        </li>
        <li>
          <svg viewBox="0 0 10 10" aria-hidden="true"><path d="M0 3.5 Q5 0 10 3.5 L8.5 5 L7 4 L7 3 Q5 2.3 3 3 L3 4 L1.5 5 Z"/><rect x="2" y="5.5" width="6" height="4" rx="0.8"/></svg>
          301.555.0147
        </li>
        <li>
          <svg viewBox="0 0 10 10" aria-hidden="true"><rect x="2.5" y="0" width="5" height="3"/><rect x="0" y="3.5" width="10" height="4" rx="0.8"/><rect x="2.5" y="7" width="5" height="3"/></svg>
          301.555.0162
        </li>
        <li>
          <svg viewBox="0 0 10 10" aria-hidden="true"><circle cx="5" cy="5" r="4.5"/><path d="M0.5 5 H9.5 M5 0.5 V9.5" stroke="#f7f7f7" stroke-width="0.8"/><ellipse cx="5" cy="5" rx="2" ry="4.5" fill="none" stroke="#f7f7f7" stroke-width="0.8"/></svg>
          www.TQSurfacing.example
        </li>
      </ul>
      <address class="contact-address">
        4187 North Calder Lane<br>
        Frederick, MD 21704
      </address>
    </div>

    <footer class="back-footer">
      <p class="services">Roads · Driveways · Brick Pavers · Seal-Coating · Concrete · Asphalt Millings</p>
      <p class="credentials">MHIC# 384072 · All Work Guaranteed · Residential &amp; Commercial</p>
    </footer>
  </section>
</main>
</body>
</html>
```